College Guide seciton 1

See the attached design. We are looking for new creative ways to display the same information/concept.

We like the fonts and colors but the layout is not intuitive, eye catching enough to prompt a college student to read through.

use exact copy

Industry/Entity Type

College

```html
<!DOCTYPE html>
<html lang="en">
<head>
<meta charset="UTF-8">
<title>College Guide – Section 02</title>
<link rel="stylesheet" href="https://fonts.googleapis.com/css2?family=Lato:wght@400;700;900&display=swap">
<style>
  :root {
    --brand-blue: #0a7fbd;
    --brand-green: #57b07f;
    --accent-mint: #a9dcc0;
    --panel-grey: #eff2f1;
    --panel-border: #e1e5e3;
    --rule-grey: #b9bfbc;
    --ink-dark: #1f2a24;
    --white: #ffffff;
    --footer-rule: #e4e6e5;
  }
  * { box-sizing: border-box; margin: 0; padding: 0; }
  html, body {
    width: 927px;
    height: 1200px;
    overflow: hidden;
    background: var(--white);
    font-family: "Lato", sans-serif;
  }
  .page {
    position: relative;
    width: 927px;
    height: 1200px;
  }

  /* Header */
  .page-header {
    position: absolute;
    top: 0; left: 0;
    width: 100%;
    height: 106px;
    background: var(--brand-blue);
    border-bottom: 7px solid var(--brand-green);
  }
  .section-number {
    position: absolute;
    left: 33px;
    top: 22px;
    font-size: 52px;
    font-weight: 700;
    line-height: 1;
    color: var(--accent-mint);
  }
  .header-divider {
    position: absolute;
    left: 124px;
    top: 12px;
    width: 5px;
    height: 75px;
    background: var(--white);
  }
  .section-title {
    position: absolute;
    left: 151px;
    top: 14px;
    font-size: 24px;
    font-weight: 700;
    line-height: 36px;
    color: var(--white);
  }

  /* Journey spine */
  .journey-spine {
    position: absolute;
    left: 461px;
    top: 140px;
    width: 5px;
    height: 985px;
    border-radius: 3px;
    background: var(--accent-mint);
  }
  .journey-stop {
    position: absolute;
    left: 452px;
    width: 23px;
    height: 23px;
    border-radius: 50%;
    background: var(--brand-blue);
    border: 4px solid var(--white);
    box-shadow: 0 0 0 3px var(--brand-green);
  }

  /* Question cards */
  .question-card {
    position: absolute;
    width: 400px;
    height: 234px;
    border-radius: 6px;
    background: var(--panel-grey);
    border: 1px solid var(--panel-border);
    box-shadow: 0 4px 10px rgba(31, 42, 36, 0.08);
  }
  .question-card.is-left { left: 38px; }
  .question-card.is-right { left: 489px; }
  .question-head {
    position: relative;
    height: 124px;
    padding: 18px 24px 0;
    background: var(--brand-green);
    border-radius: 6px 6px 0 0;
  }
  .question-title {
    font-size: 20px;
    font-weight: 900;
    line-height: 25px;
    color: var(--white);
    text-transform: uppercase;
    white-space: nowrap;
  }
  .question-hint {
    margin-top: 8px;
    font-size: 13px;
    font-weight: 700;
    line-height: 19px;
    color: var(--ink-dark);
  }
  .question-pointer {
    position: absolute;
    top: 42px;
    width: 16px;
    height: 36px;
  }
  .is-left .question-pointer { right: -16px; }
  .is-right .question-pointer { left: -16px; transform: scaleX(-1); }
  .answer-area {
    position: relative;
    height: 108px;
  }
  .answer-line {
    position: absolute;
    left: 24px;
    right: 24px;
    height: 1px;
    background: var(--rule-grey);
  }
  .answer-line:nth-child(1) { top: 32px; }
  .answer-line:nth-child(2) { top: 62px; }
  .answer-line:nth-child(3) { top: 92px; }

  /* Footer */
  .page-footer {
    position: absolute;
    left: 0;
    top: 1145px;
    width: 100%;
    border-top: 1px solid var(--footer-rule);
  }
  .page-number {
    position: absolute;
    right: 26px;
    top: 18px;
    font-size: 17px;
    font-weight: 900;
    letter-spacing: 0.5px;
    color: var(--brand-green);
  }
</style>
</head>
<body>
<div class="page">
  <header class="page-header">
    <div class="section-number">02</div>
    <div class="header-divider"></div>
    <h1 class="section-title">Take a minute to fill-in your answers to these<br>important question</h1>
  </header>

  <div class="journey-spine"></div>
  <span class="journey-stop" style="top:190px"></span>
  <span class="journey-stop" style="top:380px"></span>
  <span class="journey-stop" style="top:570px"></span>
  <span class="journey-stop" style="top:760px"></span>
  <span class="journey-stop" style="top:950px"></span>

  <section class="question-card is-left" style="top:140px">
    <div class="question-head">
      <h2 class="question-title">What is your idear college?</h2>
      <p class="question-hint">Lorem ipsum dolor sit Lorem ipsum dolor sit<br>Lorem ipsum dolor sit Lorem ipsum dolor sit<br>Lorem ipsum dolor sit Lorem ipsum dolor sit</p>
      <svg class="question-pointer" viewBox="0 0 16 36"><polygon points="0,0 16,18 0,36" fill="var(--brand-green)"/></svg>
    </div>
    <div class="answer-area"><span class="answer-line"></span><span class="answer-line"></span><span class="answer-line"></span></div>
  </section>

  <section class="question-card is-right" style="top:330px">
    <div class="question-head">
      <h2 class="question-title">What is your idear college?</h2>
      <p class="question-hint">Lorem ipsum dolor sit Lorem ipsum dolor sit<br>Lorem ipsum dolor sit Lorem ipsum dolor sit<br>Lorem ipsum dolor sit Lorem ipsum dolor sit</p>
      <svg class="question-pointer" viewBox="0 0 16 36"><polygon points="0,0 16,18 0,36" fill="var(--brand-green)"/></svg>
    </div>
    <div class="answer-area"><span class="answer-line"></span><span class="answer-line"></span><span class="answer-line"></span></div>
  </section>

  <section class="question-card is-left" style="top:520px">
    <div class="question-head">
      <h2 class="question-title">What is your idear college?</h2>
      <p class="question-hint">Lorem ipsum dolor sit Lorem ipsum dolor sit<br>Lorem ipsum dolor sit Lorem ipsum dolor sit<br>Lorem ipsum dolor sit Lorem ipsum dolor sit</p>
      <svg class="question-pointer" viewBox="0 0 16 36"><polygon points="0,0 16,18 0,36" fill="var(--brand-green)"/></svg>
    </div>
    <div class="answer-area"><span class="answer-line"></span><span class="answer-line"></span><span class="answer-line"></span></div>
  </section>

  <section class="question-card is-right" style="top:710px">
    <div class="question-head">
      <h2 class="question-title">What is your idear college?</h2>
      <p class="question-hint">Lorem ipsum dolor sit Lorem ipsum dolor sit<br>Lorem ipsum dolor sit Lorem ipsum dolor sit<br>Lorem ipsum dolor sit Lorem ipsum dolor sit</p>
      <svg class="question-pointer" viewBox="0 0 16 36"><polygon points="0,0 16,18 0,36" fill="var(--brand-green)"/></svg>
    </div>
    <div class="answer-area"><span class="answer-line"></span><span class="answer-line"></span><span class="answer-line"></span></div>
  </section>

  <section class="question-card is-left" style="top:900px">
    <div class="question-head">
      <h2 class="question-title">What is your idear college?</h2>
      <p class="question-hint">Lorem ipsum dolor sit Lorem ipsum dolor sit<br>Lorem ipsum dolor sit Lorem ipsum dolor sit<br>Lorem ipsum dolor sit Lorem ipsum dolor sit</p>
      <svg class="question-pointer" viewBox="0 0 16 36"><polygon points="0,0 16,18 0,36" fill="var(--brand-green)"/></svg>
    </div>
    <div class="answer-area"><span class="answer-line"></span><span class="answer-line"></span><span class="answer-line"></span></div>
  </section>

  <footer class="page-footer">
    <div class="page-number">PAGE : 01</div>
  </footer>
</div>
</body>
</html>
```